Lark Hoops Business card

Lark Hoops is a custom bicycle wheel builder. my current website can be viewed at www.larkhoops.us
design features i am looking for include:
Logo with font used on website(911 porsche) with a gear graphic two meshed gears maybe
black background bright green logo and name
info to include:
front
Glen Tabbert : owner/builder
ph; 555-418-7290
email sales@larkhoops.us
www.larkhoops.us
back
Brands availble:
Lark Hoops Carbon
Holt's
Meridine
Brovani
Owen Plume
Quillary
Tarn Industries
Zelvrix
Doruk
Loomcraft

```html
<!DOCTYPE html>
<html lang="en">
<head>
<meta charset="utf-8">
<title>Lark Hoops Business Card</title>
<link rel="stylesheet" href="https://fonts.googleapis.com/css2?family=Orbitron:wght@700&family=Michroma&display=swap">
<style>
  :root {
    --backdrop: #2a2a2a;
    --card-top: #262626;
    --card-mid: #1c1c1c;
    --card-dark: #111111;
    --rule: #3a3a3a;
    --brand-green: #2bff1c;
    --icon-green: #35e62a;
    --silver: #d8d8d8;
    --contact-text: #e6e6e6;
  }
  * { margin: 0; padding: 0; box-sizing: border-box; }
  html, body {
    width: 1200px; height: 1000px; overflow: hidden;
    background: var(--backdrop);
  }
  .card {
    position: absolute; left: 228px; top: 298px;
    width: 764px; height: 434px;
    background: var(--card-mid);
    overflow: hidden;
  }
  .card-header {
    position: absolute; left: 0; top: 0; width: 100%; height: 80px;
    background: linear-gradient(180deg, #2c2c2c 0%, var(--card-top) 60%, #1e1e1e 100%);
    border-bottom: 2px solid var(--rule);
  }
  .card-body {
    position: absolute; left: 0; top: 82px; width: 100%; height: 266px;
    background: radial-gradient(ellipse 60% 70% at 50% 45%, #333 0%, #222 55%, #181818 100%);
  }
  .card-footer {
    position: absolute; left: 0; top: 348px; width: 100%; height: 86px;
    background: linear-gradient(180deg, #222 0%, var(--card-dark) 12%, #151515 100%);
    border-top: 2px solid var(--rule);
  }
  .brand-mark {
    position: absolute; left: 316px; top: 118px;
    width: 136px; height: 136px; border-radius: 50%;
    background: var(--brand-green);
  }
  .brand-name {
    position: absolute; left: 0; top: 268px; width: 100%; text-align: center;
    font-family: 'Orbitron', sans-serif; font-weight: 700;
    font-size: 25px; letter-spacing: 11px; padding-left: 11px; line-height: 1;
    color: var(--brand-green); text-transform: uppercase;
  }
  .owner-name {
    position: absolute; left: 0; top: 293px; width: 100%; text-align: center;
    font-family: 'Orbitron', sans-serif; font-weight: 700;
    font-size: 16px; letter-spacing: 10px; padding-left: 10px; line-height: 1;
    color: var(--silver); text-transform: uppercase;
  }
  .owner-role {
    position: absolute; right: 244px; top: 310px;
    font-family: 'Michroma', sans-serif; font-size: 9px; letter-spacing: 1.5px;
    color: var(--brand-green); text-transform: uppercase;
  }
  .contact {
    position: absolute; top: 385px;
    display: flex; align-items: center; gap: 12px;
    font-family: 'Michroma', sans-serif; font-size: 10px; letter-spacing: 1px;
    color: var(--contact-text); text-transform: uppercase; white-space: nowrap;
  }
  .contact svg { width: 16px; height: 14px; fill: var(--icon-green); flex: none; }
  .contact-phone { left: 42px; font-size: 11.5px; letter-spacing: 1.5px; }
  .contact-email { left: 248px; }
  .contact-web { left: 521px; }
</style>
</head>
<body>
  <article class="card">
    <div class="card-header"></div>
    <div class="card-body"></div>
    <div class="card-footer"></div>

    <span class="brand-mark" aria-hidden="true"></span>
    <p class="brand-name">Lark Hoops</p>
    <p class="owner-name">Glen Tabbert</p>
    <p class="owner-role">Owner/Builder</p>

    <p class="contact contact-phone">
      <svg viewBox="0 0 16 14" aria-hidden="true">
        <path d="M1 4 Q8 0 15 4 L15 6 L11 6 L11 4.5 Q8 3.5 5 4.5 L5 6 L1 6 Z"/>
        <path d="M3 7 L13 7 L14 13 L2 13 Z"/>
      </svg>
      555-418-7290
    </p>
    <p class="contact contact-email">
      <svg viewBox="0 0 16 12" aria-hidden="true">
        <path d="M0 1 L16 1 L16 11 L0 11 Z M1.5 2 L8 7 L14.5 2 Z" fill-rule="evenodd"/>
      </svg>
      sales@larkhoops.us
    </p>
    <p class="contact contact-web">
      <svg viewBox="0 0 16 16" aria-hidden="true">
        <circle cx="8" cy="8" r="7" fill="none" stroke="#35e62a" stroke-width="1.4"/>
        <ellipse cx="8" cy="8" rx="3" ry="7" fill="none" stroke="#35e62a" stroke-width="1.2"/>
        <path d="M1 8 H15 M2.5 4.5 H13.5 M2.5 11.5 H13.5" stroke="#35e62a" stroke-width="1.1"/>
      </svg>
      www.larkhoops.us
    </p>
  </article>
</body>
</html>
```